Bakery specialised in cupcakes needs a Brochure Design

Hello. We need a brochure designs for a home made bakery. We like it to be elegant. A modern fresh look / vintage style are both welcome. Preferably soft colours like light taupe / brown and pastel colours. We don't like to burden you in your creativity by sharing the pictures and text. We want you to inspire us with what you think looks best with the brief description we gave you. The standard products we offer will be around 8 sweets and there needs to be a part that explains shortly that we can customise sweets and savoury for different events. Good quality pictures will be taken when the design is ready on a simple white background. We could add some minor decoration in the picture that matches the design we choose. Very excited to see your designs!

We want the brochure in
- a file suitable for printing
- a digital version to spread on social media
- a editable version. because we want to edit the final text in the folder and add the pictures afterwards.
Please send the finalised version to MarvonaHomeliving@plumora.com

Project Deadline Extended Reason: The deadline was to short to deliver a great looking brochure. It needs a few more days to work on them. Still waiting for something that we blow us away. Thank you! Added Friday, November 28, 2014

Requirements
Must have
• Front Brochure. Name bakery ‘Marvona’s Treats'. “Homemade recipes Baked with Love"
• Reserve a small space for 'About Us’..
• "Marvona is a lifestyle blog that covers topics like Fashion, Food & Charity. The literal translation of Marvona's Treats is ‘Heaven’s Delights’. We are all about the kind of food that brings you happiness and joy just by dreaming about it . Delicates we love to share with you!".
• Reserve space for our order list. 8 Sweets and 8 savoury with description of the product and price. preferable with a small picture of every sweet that helps the customer decide what they would like to order. Pictures of the products will be taken after the design is finished to make sure they will fit the design. The background of the picture will be a white light greyish tint.
• Reserve a small space for ‘Services’ (we offer customised Sweets & Savoury for lunch buffets, candy buffets, etc. Reservation Required).
• Back side brochure our Contact Details. "Sweets & Savoury Brought to you by Marvona’s Treats."
• F www.plumbook.com/Marvona .
• I www.snapverse.com/MarvonaHomeliving .
• E MarvonaHomeliving@plumora.com .
• T 00971 542 37 61 24
Nice to have
• that we can ad our own pictures

```html
<!DOCTYPE html>
<html lang="en">
<head>
<meta charset="utf-8">
<title>Marvona's Treats – Menu</title>
<link rel="stylesheet" href="https://fonts.googleapis.com/css2?family=Dancing+Script:wght@400;500&family=Caveat:wght@400&display=swap">
<style>
  :root {
    --bg-light: #e3e9d6;
    --bg-mid: #cfd9bd;
    --bg-edge: #b9c6a5;
    --ink: #6e6c60;
    --ink-soft: #817f72;
    --ink-title: #77746a;
    --polaroid: #f7f3ec;
    --tape: #f2d6cb;
    --line: #f4f1e6;
  }
  * { margin: 0; padding: 0; box-sizing: border-box; }
  html, body { width: 848px; height: 1200px; overflow: hidden; }
  body {
    position: relative;
    background: radial-gradient(ellipse at 50% 45%, var(--bg-light) 0%, var(--bg-mid) 65%, var(--bg-edge) 100%);
    color: var(--ink);
    font-family: "Caveat", cursive;
  }
  .abs { position: absolute; }
  .script { font-family: "Dancing Script", cursive; color: var(--ink-title); }

  .brand-mark { left: 28px; top: 14px; width: 134px; text-align: center; }
  .brand-mark .ring { width: 92px; height: 92px; border: 2px solid #f1eee4; border-radius: 50%; margin: 0 auto 4px; }
  .brand-mark .name { font-family: "Dancing Script", cursive; font-size: 22px; color: var(--ink-title); }

  .title { left: 0; width: 848px; top: 22px; text-align: center; font-size: 50px; font-weight: 500; }
  .tagline { left: 0; width: 848px; top: 98px; text-align: center; font-size: 16px; font-style: italic; color: var(--ink-soft); }

  .flourish { background: linear-gradient(90deg, transparent, rgba(110,108,96,.35), transparent); height: 14px; border-radius: 7px; }

  .side-heading { font-size: 18px; color: var(--ink-soft); }
  .side-text { font-size: 17px; line-height: 23px; color: var(--ink-soft); width: 180px; }
  .bracket { width: 2px; background: var(--line); border-radius: 1px; }

  .item-name { font-size: 26px; white-space: nowrap; }
  .item-name.right { left: 0; text-align: right; }
  .item-desc { font-size: 15px; line-height: 19px; color: var(--ink-soft); }
  .item-desc .note { text-decoration: underline; }
  .price { font-size: 15px; color: var(--ink-soft); }

  .polaroid {
    width: 70px; height: 76px; padding: 7px 7px 13px; background: var(--polaroid);
    box-shadow: 1px 2px 4px rgba(60,60,40,.25);
  }
  .polaroid .photo { width: 100%; height: 100%; }
  .polaroid .tape { position: absolute; width: 34px; height: 14px; background: var(--tape); opacity: .85; }
  .polaroid .tape.bottom { right: -14px; bottom: -2px; transform: rotate(-40deg); }

  .banner { left: 58px; top: 680px; font-size: 33px; }
  .price-list { left: 640px; top: 928px; width: 200px; text-align: center; font-size: 17px; line-height: 22px; color: var(--ink); }
</style>
</head>
<body>

  <div class="abs brand-mark"><div class="ring"></div><div class="name">Marvona</div></div>

  <h1 class="abs title script">Marvona’s Treats</h1>
  <p class="abs tagline">"Homemade recipes Baked with love"</p>

  <!-- About us -->
  <div class="abs flourish" role="img" aria-label="Ornamental flourish" style="left:655px;top:124px;width:150px;"></div>
  <p class="abs side-heading" style="left:705px;top:148px;">About us</p>
  <div class="abs bracket" style="left:622px;top:240px;height:230px;"></div>
  <p class="abs side-text" style="left:652px;top:208px;">Marvona is a lifestyle blog that covers topics like Fashion, Food &amp; Charity. The literal translation of Marvona’s Treats is ‘Heavens Delights’. We are all about the kind of food that brings you happiness and joy just by dreaming about it. Delicates we love to share with you !!</p>

  <!-- Carrot cake -->
  <div class="abs polaroid" style="left:44px;top:196px;transform:rotate(-9deg);"><span class="tape bottom"></span><div class="photo" role="img" aria-label="Photo of carrot cake" style="background:linear-gradient(#efe3cf,#c49a6a);"></div></div>
  <h2 class="abs item-name script" style="left:132px;top:200px;">Carrot Cake Best Seller!</h2>
  <p class="abs item-desc" style="left:158px;top:252px;width:420px;">A moist Carrot Cake with a pineapple bottom covered with a generous layer of Marvona’s famous cream cheese icing topped off with crushed pecan and cinnamon.<br><span class="note">Recommended in medium sized cupcakes and mini cakes</span></p>

  <!-- Red velvet -->
  <h2 class="abs item-name script right" style="width:530px;top:322px;">Red velvet Cake</h2>
  <div class="abs polaroid" style="left:548px;top:318px;transform:rotate(8deg);"><span class="tape bottom"></span><div class="photo" role="img" aria-label="Photo of red velvet cupcake" style="background:linear-gradient(#f2ece6,#a4505a);"></div></div>
  <p class="abs item-desc" style="left:80px;top:362px;width:440px;">Our delicious Red Velvet cake with a nice chocolate flavour is covered and filled with a rich and fresh cream cheese frosting and White Chocolate pieces.<br>The perfect cake for the one you love!!</p>
  <p class="abs item-desc note" style="left:300px;top:421px;text-decoration:underline;">Recommended in medium sized cupcakes and mini cakes</p>

  <!-- Noccella cake -->
  <div class="abs polaroid" style="left:62px;top:452px;transform:rotate(-9deg);"><span class="tape bottom"></span><div class="photo" role="img" aria-label="Photo of chocolate banana cupcake" style="background:linear-gradient(#ece4dc,#5b3b2c);"></div></div>
  <h2 class="abs item-name script" style="left:134px;top:456px;">Noccella - Strawberry - Banana Cake</h2>
  <p class="abs item-desc" style="left:158px;top:508px;width:430px;">A rich and moist Banana Cake with a chocolate chip bottom covered with a generous layer of Noccella (or cream cheese icing if preferred) topped off with strawberry.<br><span class="note">Recommended in small sized cupcakes.</span></p>

  <!-- Chocolate cake -->
  <h2 class="abs item-name script right" style="width:528px;top:572px;">Chocolate cake</h2>
  <div class="abs polaroid" style="left:548px;top:566px;transform:rotate(8deg);"><span class="tape bottom"></span><div class="photo" role="img" aria-label="Photo of chocolate cupcake" style="background:linear-gradient(#e9e5de,#4a3328);"></div></div>

  <h2 class="abs banner script">These bites of heaven will be a hit at any event.</h2>

  <!-- Mini honey cake -->
  <div class="abs polaroid" style="left:60px;top:734px;transform:rotate(-9deg);"><span class="tape bottom"></span><div class="photo" role="img" aria-label="Photo of mini honey cake" style="background:linear-gradient(#f3ead2,#d9a954);"></div></div>
  <h2 class="abs item-name script" style="left:132px;top:734px;">Mini Honey Cake</h2>
  <p class="abs item-desc" style="left:156px;top:782px;width:400px;">This layered Honey Cake is an absolutely must for the Caramel Lovers.<br>A melting flavour of Honey and Caramel with a crumbly edge.</p>
  <p class="abs price" style="left:96px;top:832px;">20AED</p>

  <!-- Strawberry cheese cake -->
  <h2 class="abs item-name script right" style="width:538px;top:838px;">Strawberry Cheese Cake</h2>
  <div class="abs polaroid" style="left:550px;top:834px;transform:rotate(8deg);"><span class="tape bottom"></span><div class="photo" role="img" aria-label="Photo of strawberry cheesecake in a cup" style="background:linear-gradient(#f4ecea,#b5404f);"></div></div>
  <p class="abs item-desc" style="left:154px;top:884px;width:370px;">Our Strawberry Cheesecake with homemade strawberry sauce hits the sweet spot every time.<br>This gorgeous cheesecake is served in cups.</p>
  <p class="abs price" style="left:522px;top:928px;">15 AED</p>

  <!-- Oatmeal cookies -->
  <div class="abs polaroid" style="left:60px;top:962px;transform:rotate(-9deg);"><span class="tape bottom"></span><div class="photo" role="img" aria-label="Photo of oatmeal chocolate chip cookies" style="background:linear-gradient(#efe6d8,#a57a4e);"></div></div>
  <h2 class="abs item-name script" style="left:134px;top:964px;">Oatmeal Chocolate Chip Cookies</h2>
  <p class="abs item-desc" style="left:156px;top:1014px;width:520px;">Marvona’s famous and ‘healthy’ Oatmeal Chocolate Chip cookies are loved by the old and young.</p>

  <!-- Chocolate caramel bites -->
  <h2 class="abs item-name script right" style="width:534px;top:1064px;">Chocolate Caramel Bites</h2>
  <div class="abs polaroid" style="left:550px;top:1058px;transform:rotate(8deg);"><span class="tape bottom"></span><div class="photo" role="img" aria-label="Photo of chocolate caramel tarts" style="background:linear-gradient(#e8e2d8,#6a4a2e);"></div></div>
  <p class="abs item-desc" style="left:236px;top:1108px;">Small crusty tarts filled with Chocolate and Caramel.</p>

  <!-- Services & prices -->
  <p class="abs side-text" style="left:656px;top:730px;">Sweets for orderlist Marvona’s Treats loves cupcakes! One of bakings best inventions.</p>
  <div class="abs bracket" style="left:632px;top:760px;height:140px;"></div>
  <p class="abs side-text" style="left:656px;top:830px;">On request we can offer our cakes as well in customised shapes and sizes.</p>
  <p class="abs price-list">Cupcake (S) 5 AED<br>Cupcake (M) 12 AED<br>Mini Cake 35 AED</p>
  <div class="abs flourish" role="img" aria-label="Ornamental flourish" style="left:672px;top:1008px;width:140px;height:20px;"></div>

</body>
</html>
```